Quarrytide
Quarrytide - Financial Services
Financial Services
www.quarrytidepay.com
Our team has been providing solutions for workers compensation for business owners for over 22 years, our service is provoided at no charge (as it is paid for by the vendor). What makes us unique is our ability to write just about every size company (3 man to 1000) and industry in every state,. Our programs simlyfy the business owners way of doing business by eliminationg several annoying functions that business owners face. For example, with our program a business owner would write one check for payroll, that check would cover his payroll, workers compensation, payroll taxes, employee deductions and garnishments, direct deposit and benefit deductions, year end W-2's and the liabilities that come with year end W-2's. Our program we keeps business owners compliant by keeping them informed about new requirements, labor laws, we provide all employee applications, safety posters, they are able to call with any employee related questions about hiring and firing and so on. All usually for less that they can do it themselves.
Busy, wordy
Service Oriented
White/possible grey, logo colors
Blues and whites and greys, logo colors
left side
We have a content writer completing the text, our home page will contain very little text and focus more as a landing page. The site itself needs to be very clean, simple and easy to navigate but will also allow viewers to go deep into the site if they want to find information, yet at the same time it will not force people away because of too much content

```html
<!DOCTYPE html>
<html lang="en">
<head>
<meta charset="utf-8">
<title>Quarrytide - Financial Services</title>
<link href="https://fonts.googleapis.com/css2?family=Arimo:wght@400;700&family=Tinos:wght@700&display=swap" rel="stylesheet">
<style>
  :root {
    --navy: #0c3a78;
    --blue: #1a6fc4;
    --sky: #5eb3ea;
    --ice: #dcecf7;
    --ink: #3a3a3a;
    --muted: #666a70;
    --grey-dark: #4a4c50;
    --grey-mid: #8c8f94;
    --grey-light: #e9eaec;
    --white: #ffffff;
  }
  * { box-sizing: border-box; margin: 0; padding: 0; }
  html, body { width: 1200px; height: 845px; overflow: hidden; background: var(--white); }
  body { font-family: "Arimo", Arial, sans-serif; color: var(--ink); position: relative; }

  .site-header { position: absolute; top: 0; left: 0; width: 1200px; height: 108px; background: var(--white); }
  .brand { position: absolute; left: 150px; top: 16px; display: flex; align-items: center; gap: 14px; }
  .brand-mark { width: 58px; height: 58px; border-radius: 50%; background: var(--blue); flex: none; }
  .brand-name { font-size: 34px; font-weight: 700; color: var(--navy); letter-spacing: 0.5px; white-space: nowrap; }

  .main-nav { position: absolute; left: 494px; top: 0; width: 543px; height: 50px;
    background: linear-gradient(#1f5fa8, var(--navy)); border-radius: 0 0 14px 14px;
    display: flex; align-items: center; padding-left: 8px; }
  .main-nav a { color: var(--white); text-decoration: none; font-size: 15px; padding: 0 17px;
    height: 50px; line-height: 52px; white-space: nowrap; flex: none; }
  .main-nav a.is-active { background: rgba(255,255,255,0.28); }

  .hero-band { position: absolute; top: 108px; left: 0; width: 1200px; height: 300px;
    background: linear-gradient(var(--ice), #eef5fb 60%, var(--white)); }
  .hero-fade { position: absolute; top: 408px; left: 0; width: 1200px; height: 50px;
    background: linear-gradient(var(--grey-light), var(--white)); }
  .hero { position: absolute; left: 149px; top: 108px; width: 900px; height: 300px; overflow: hidden; }
  .hero-visual { position: absolute; inset: 0;
    background: linear-gradient(100deg, #2a7fcf 0%, var(--sky) 35%, #3a8ed8 60%, #0f4a92 100%); }
  .hero-copy { position: absolute; right: 20px; bottom: 14px; text-align: right; color: var(--white);
    font-family: "Tinos", "Times New Roman", serif; font-weight: 700; text-shadow: 0 1px 3px rgba(0,0,0,0.4); }
  .hero-tagline { font-size: 30px; margin-bottom: 20px; }
  .hero-call { font-size: 21px; }
  .hero-phone { font-size: 31px; }

  .welcome { position: absolute; left: 149px; top: 458px; width: 670px; }
  .welcome h1 { font-size: 27px; font-weight: 400; color: #222; display: flex; align-items: center; gap: 12px; margin-bottom: 12px; }
  .welcome h1 .dot { width: 26px; height: 26px; border-radius: 50%; background: var(--blue); }
  .welcome h1 strong { color: var(--navy); font-weight: 700; }
  .welcome p { font-size: 13.5px; line-height: 19px; color: var(--muted); margin-bottom: 19px; }
  .highlights { list-style: none; margin-top: 4px; }
  .highlights li { font-size: 13.5px; line-height: 22px; color: var(--muted); padding-left: 28px; position: relative; }
  .highlights li::before { content: ""; position: absolute; left: 4px; top: 7px; border-left: 8px solid var(--blue);
    border-top: 4px solid transparent; border-bottom: 4px solid transparent; }

  .contact-card { position: absolute; left: 852px; top: 461px; width: 197px; height: 260px;
    background: var(--white); box-shadow: 0 2px 8px rgba(0,0,0,0.25); }
  .contact-head { height: 34px; background: linear-gradient(#3c3e42, #1f2023); color: var(--white);
    font-size: 19px; display: flex; align-items: center; gap: 10px; padding-left: 10px; }
  .contact-form { padding: 10px 12px; }
  .contact-form label { display: block; font-size: 10px; color: #444; margin-top: 4px; }
  .contact-form .field { height: 18px; border: 1px solid #b9bbbe; background: #f4f4f4; margin-top: 2px; }
  .contact-form .field.tall { height: 54px; }
  .contact-submit { display: flex; justify-content: flex-end; margin-top: 10px; }
  .contact-submit span { background: #2b2c2f; color: var(--white); font-size: 11px; font-weight: 700; padding: 3px 8px 3px 18px; position: relative; }
  .contact-submit span::before { content: ""; position: absolute; left: 6px; top: 6px; border-left: 6px solid var(--white);
    border-top: 3px solid transparent; border-bottom: 3px solid transparent; }

  .site-footer { position: absolute; left: 0; top: 756px; width: 1200px; height: 89px;
    background: linear-gradient(var(--grey-mid), var(--grey-dark) 30%); }
  .footer-links { position: absolute; left: 152px; top: 26px; font-size: 12px; color: var(--white); }
  .footer-links a { color: var(--white); text-decoration: none; }
  .footer-links .sep { margin: 0 6px; }
  .footer-copy { position: absolute; left: 152px; top: 54px; font-size: 11px; color: #d8d8d8; }
  .footer-brand { position: absolute; left: 848px; top: 18px; display: flex; align-items: center; gap: 10px; }
  .footer-brand .brand-mark { width: 48px; height: 48px; background: var(--sky); }
  .footer-brand .brand-name { font-size: 26px; color: var(--white); }
</style>
</head>
<body>
  <header class="site-header">
    <div class="brand">
      <span class="brand-mark"></span>
      <span class="brand-name">QUARRYTIDE</span>
    </div>
    <nav class="main-nav">
      <a href="#" class="is-active">HOME</a>
      <a href="#">ABOUT US</a>
      <a href="#">SERVICES</a>
      <a href="#">HELP</a>
      <a href="#">CONTACT US</a>
    </nav>
  </header>

  <div class="hero-band"></div>
  <div class="hero-fade"></div>
  <section class="hero">
    <div class="hero-visual" role="img" aria-label="Blue world map banner divided into vertical panels"></div>
    <div class="hero-copy">
      <div class="hero-tagline">Solution-Oriented</div>
      <div class="hero-call">Call us at:</div>
      <div class="hero-phone">(480)-555-0137</div>
    </div>
  </section>

  <main class="welcome">
    <h1><span class="dot"></span>Welcome to <strong>QUARRYTIDE</strong></h1>
    <p>Maecenas vestibulum nibh sed lectus vulputate quis eleifend velit placerat. Phasellus dictum, mauris at dignissim tincidunt, erat quam mattis nisl, quis condimentum mauris orci non massa.</p>
    <p>Nunc neque felis, pellentesque sit amet congue eget, interdum at magna. Donec tincidunt rutrum diam eget fringilla. Pellentesque nec magna sit amet metus congue convallis.</p>
    <ul class="highlights">
      <li>Curabitur iaculis metus vitae arcu vestibulum sagittis.</li>
      <li>Bras dapibus dapibus mauris, a porta odio placerat quis.</li>
      <li>Sed sed lorem id ipsum congue euismod.</li>
      <li>Htiam fringilla sem sit amet nulla lobortis hendrerit sit amet eu odio.</li>
    </ul>
  </main>

  <aside class="contact-card">
    <div class="contact-head">
      <svg width="26" height="18" viewBox="0 0 26 18" aria-hidden="true">
        <rect x="1" y="1" width="24" height="16" fill="#fff" stroke="#999"/>
        <polyline points="1,1 13,10 25,1" fill="none" stroke="#999"/>
      </svg>
      CONTACT US
    </div>
    <form class="contact-form">
      <label>Name*</label><div class="field"></div>
      <label>Phone*</label><div class="field"></div>
      <label>Email*</label><div class="field"></div>
      <label>Question/Comment</label><div class="field tall"></div>
      <div class="contact-submit"><span>Submit</span></div>
    </form>
  </aside>

  <footer class="site-footer">
    <div class="footer-links">
      <a href="#">Home</a><span class="sep">|</span><a href="#">About Us</a><span class="sep">|</span><a href="#">Services</a><span class="sep">|</span><a href="#">Help</a><span class="sep">|</span><a href="#">Contact Us</a>
    </div>
    <div class="footer-copy">Copyright (c) QUARRYTIDE. All rights reserved.</div>
    <div class="footer-brand">
      <span class="brand-mark"></span>
      <span class="brand-name">QUARRYTIDE</span>
    </div>
  </footer>
</body>
</html>
```